We need motivational posters designed to be used in classrooms at a truck driving school. The purpose of the posters is to motivate the students.

I want the the quotes to be the main focal point of emphasis and our logo on the bottom of the poster for branding purposes.

I would like the images to be related to the trucking industry

Below are the quotes for the posters

Poster 1
"Start where you are. Use what you have. Do what you can."
-Delmar Quisby-

Poster 2
"The secret of getting ahead is getting started"
-Owen Farrow-

Poster 3
"Most effective way to do it, is to do it."
-Rosalind Pemberly-

Poster 4
"Set your goals big, and don't stop till you get there."
-Cy Whitlock-

Poster 5
"If you are not willing to learn, no one can help you. If you are determined to learn, no one can stop you."
-Unknown-

Poster 6
"The will to succeed is important, but what's more important is the will to prepare."
-Dougie Hallam-

THESE POSTERS SHOULD BE DESIGNED AS 18X24
LANDSCAPE AND PORTRAIT ORIENTATION

Industry/Entity Type

School

```html
<!DOCTYPE html>
<html lang="en">
<head>
<meta charset="utf-8">
<title>Start Where You Are – Classroom Poster</title>
<link rel="stylesheet" href="https://fonts.googleapis.com/css2?family=Bebas+Neue&display=swap">
<style>
  :root {
    --paper: #ffffff;
    --lime: #c2cd2f;
    --sky: #7fc1c9;
    --rust: #d75f1f;
    --stone: #9a9a9a;
    --navy: #1f2f4a;
    --band-sky-top: #8fb4d6;
    --band-sky-low: #dfe8ef;
    --band-field: #7f8f5a;
    --band-road: #b9b9b4;
  }
  html, body {
    margin: 0;
    padding: 0;
    width: 800px;
    height: 1200px;
    overflow: hidden;
    background: var(--paper);
  }
  .poster {
    position: relative;
    width: 800px;
    height: 1200px;
    background: var(--paper);
    font-family: "Bebas Neue", "Arial Narrow", sans-serif;
    overflow: hidden;
  }
  .quote-mark {
    position: absolute;
    width: 98px;
    height: 86px;
  }
  .quote-mark--open { left: 52px; top: 88px; }
  .quote-mark--close { left: 42px; top: 838px; }
  .quote-line {
    position: absolute;
    margin: 0;
    line-height: 1;
    white-space: nowrap;
    font-weight: 400;
  }
  .quote-line--lead {
    left: 50px;
    font-size: 166px;
    color: var(--lime);
  }
  .quote-line--one { top: 188px; }
  .quote-line--two { top: 382px; }
  .quote-line--use {
    left: 50px;
    top: 556px;
    font-size: 112px;
    color: var(--sky);
  }
  .quote-line--do {
    left: 40px;
    top: 689px;
    font-size: 118px;
    color: var(--rust);
  }
  .attribution {
    position: absolute;
    right: 74px;
    top: 1027px;
    margin: 0;
    font-size: 56px;
    line-height: 1;
    color: var(--stone);
    letter-spacing: 1px;
  }
  .brand-band {
    position: absolute;
    left: 0;
    bottom: 0;
    width: 800px;
    height: 101px;
  }
  .brand-band__scene {
    position: absolute;
    inset: 0;
    background: linear-gradient(to bottom,
      var(--band-sky-top) 0%,
      var(--band-sky-low) 62%,
      var(--band-field) 80%,
      var(--band-road) 88%,
      var(--band-road) 100%);
  }
  .brand-band__truck {
    position: absolute;
    left: 468px;
    top: 23px;
    width: 297px;
    height: 62px;
    background: linear-gradient(to bottom, #e9ecee, #c6cbcf);
    border-radius: 3px;
  }
  .brand-mark {
    position: absolute;
    left: 46px;
    top: 30px;
    display: flex;
    align-items: center;
    gap: 8px;
  }
  .brand-mark__dot {
    width: 40px;
    height: 40px;
    border-radius: 50%;
    background: var(--navy);
  }
  .brand-mark__name {
    font-size: 20px;
    line-height: 1;
    color: var(--navy);
    letter-spacing: 0.5px;
  }
</style>
</head>
<body>
  <main class="poster">
    <svg class="quote-mark quote-mark--open" viewBox="0 0 98 86" aria-hidden="true">
      <polygon points="0,0 38,0 33,86 8,86" fill="var(--lime)"/>
      <polygon points="58,0 96,0 91,86 66,86" fill="var(--lime)"/>
    </svg>

    <p class="quote-line quote-line--lead quote-line--one">Start where</p>
    <p class="quote-line quote-line--lead quote-line--two">you are.</p>
    <p class="quote-line quote-line--use">Use what you have.</p>
    <p class="quote-line quote-line--do">Do what you can.</p>

    <svg class="quote-mark quote-mark--close" viewBox="0 0 98 86" aria-hidden="true">
      <polygon points="0,0 38,0 33,86 8,86" fill="var(--rust)"/>
      <polygon points="60,0 98,0 93,86 68,86" fill="var(--rust)"/>
    </svg>

    <p class="attribution">-Delmar Quisby-</p>

    <footer class="brand-band">
      <div class="brand-band__scene" role="img" aria-label="Photo of a semi truck with a white trailer driving on an open highway under a blue sky"></div>
      <div class="brand-band__truck" role="img" aria-label="White tractor-trailer on the road"></div>
      <div class="brand-mark">
        <span class="brand-mark__dot"></span>
        <span class="brand-mark__name">Keystone Truck Driving School, LLC</span>
      </div>
    </footer>
  </main>
</body>
</html>
```